Clear sticker design for packaging

I need 4” diameter clear stickers designed for birthdays, thank you , teachers day and all the other special days to complete my gift packaging. They will go on the top of each tube to differentiate each gift for each occasion. Our design is on craft paper and I’ve uploaded a few examples of what we are trying to achieve. Last picture is the top of our tube where the stickers will be placed. We don’t want too much color unless for Christmas and Valentine’s Day maybe! We are working with black and gold or a mixture of both mostly

```html
<!DOCTYPE html>
<html lang="en">
<head>
<meta charset="utf-8">
<title>Occasion Stickers</title>
<link rel="stylesheet" href="https://fonts.googleapis.com/css2?family=Allura&family=Bungee+Inline&family=Bungee+Outline&family=Gochi+Hand&family=Great+Vibes&family=Kaushan+Script&family=Rye&display=swap">
<style>
  :root {
    --paper: #ffffff;
    --edge: #dcdcdc;
    --ink: #111111;
    --gold-dark: #6e6452;
    --gold-mid: #b39a4a;
    --gold-bright: #e8c12c;
  }
  html, body {
    margin: 0;
    padding: 0;
    width: 1200px;
    height: 1200px;
    overflow: hidden;
    background: var(--paper);
  }
  .sheet { display: block; width: 1200px; height: 1200px; }
  .sticker-edge { fill: var(--paper); stroke: var(--edge); stroke-width: 1.5; }
  .ring-gold { fill: none; stroke: url(#gold); }
  .ring-ink { fill: none; stroke: var(--ink); }
  .gold-text { fill: url(#gold); }
  .ink-text { fill: var(--ink); }
  .script-fine { font-family: "Great Vibes", cursive; }
  .block-inline { font-family: "Bungee Inline", sans-serif; }
  .block-outline { font-family: "Bungee Outline", sans-serif; }
  .circus { font-family: "Rye", serif; }
  .hand { font-family: "Gochi Hand", cursive; }
  .brush { font-family: "Kaushan Script", cursive; }
  .script-love { font-family: "Allura", cursive; }
</style>
</head>
<body>
<svg class="sheet" viewBox="0 0 1200 1200" xmlns="http://www.w3.org/2000/svg">
  <defs>
    <linearGradient id="gold" x1="0" y1="1" x2="1" y2="0">
      <stop offset="0" stop-color="#6e6452"/>
      <stop offset="0.55" stop-color="#e8c12c"/>
      <stop offset="1" stop-color="#8a7d5c"/>
    </linearGradient>
    <radialGradient id="festive-tone" cx="0.5" cy="0.6" r="0.6">
      <stop offset="0" stop-color="#f2cc2a"/>
      <stop offset="1" stop-color="#a88f45"/>
    </radialGradient>
    <path id="teacher-arc" d="M150,520 A90,90 0 0 1 300,520"/>
    <path id="merry-arc" d="M489,946 A80,80 0 0 1 649,946"/>
    <path id="christmas-arc" d="M454,946 A115,115 0 1 0 677,907"/>
  </defs>

  <!-- Happy Birthday -->
  <g class="sticker sticker-birthday">
    <circle class="sticker-edge" cx="234" cy="244" r="139"/>
    <circle class="ring-gold" cx="234" cy="244" r="127" stroke-width="3"/>
    <circle class="ring-gold" cx="234" cy="244" r="120" stroke-width="1.5"/>
    <text class="gold-text script-fine" x="226" y="226" font-size="66" text-anchor="middle">Happy</text>
    <text class="gold-text script-fine" x="234" y="300" font-size="62" text-anchor="middle">Birthday</text>
  </g>

  <!-- Thank You, black -->
  <g class="sticker sticker-thanks-ink">
    <circle class="sticker-edge" cx="570" cy="244" r="139"/>
    <circle class="ring-ink" cx="570" cy="244" r="126" stroke-width="3"/>
    <circle class="ring-ink" cx="570" cy="244" r="119" stroke-width="1.2"/>
    <text class="ink-text block-inline" x="570" y="248" font-size="54" text-anchor="middle">THANK</text>
    <text class="ink-text block-inline" x="570" y="298" font-size="50" text-anchor="middle">YOU</text>
  </g>

  <!-- Thank You, gold -->
  <g class="sticker sticker-thanks-gold">
    <circle class="sticker-edge" cx="936" cy="256" r="139"/>
    <circle class="ring-gold" cx="936" cy="256" r="127" stroke-width="3"/>
    <circle class="ring-gold" cx="936" cy="256" r="120" stroke-width="1.5"/>
    <text class="gold-text circus" x="940" y="234" font-size="50" text-anchor="middle">Thank</text>
    <text class="gold-text circus" x="932" y="312" font-size="66" text-anchor="middle">You</text>
  </g>

  <!-- Happy Teacher's Day -->
  <g class="sticker sticker-teachers-day">
    <circle class="sticker-edge" cx="225" cy="565" r="139"/>
    <circle class="ring-ink" cx="225" cy="565" r="127" stroke-width="3"/>
    <circle class="ring-ink" cx="225" cy="565" r="120" stroke-width="1.2"/>
    <text class="ink-text hand" font-size="40"><textPath href="#teacher-arc" startOffset="50%" text-anchor="middle">HaPPy</textPath></text>
    <text class="ink-text hand" x="225" y="588" font-size="46" text-anchor="middle">TEACHER'S</text>
    <text class="ink-text hand" x="228" y="652" font-size="46" text-anchor="middle">Day</text>
  </g>

  <!-- Happy Thanksgiving -->
  <g class="sticker sticker-thanksgiving">
    <circle class="sticker-edge" cx="569" cy="563" r="137"/>
    <g transform="rotate(-6 569 563)">
      <text class="ink-text brush" x="568" y="530" font-size="52" text-anchor="middle">happy</text>
      <text class="ink-text brush" x="562" y="584" font-size="56" text-anchor="middle">thanks</text>
      <text class="ink-text brush" x="578" y="636" font-size="54" text-anchor="middle">giving</text>
    </g>
  </g>

  <!-- Best Teacher Ever -->
  <g class="sticker sticker-best-teacher">
    <circle class="sticker-edge" cx="923" cy="563" r="137"/>
    <g transform="rotate(-8 923 563)">
      <text class="gold-text brush" x="888" y="530" font-size="56" text-anchor="middle">best</text>
      <text class="gold-text brush" x="920" y="594" font-size="60" text-anchor="middle">teacher</text>
      <text class="gold-text brush" x="950" y="654" font-size="56" text-anchor="middle">ever!</text>
    </g>
  </g>

  <!-- To My Valentine -->
  <g class="sticker sticker-valentine">
    <circle class="sticker-edge" cx="225" cy="943" r="137"/>
    <text class="gold-text script-love" x="220" y="918" font-size="44" text-anchor="middle" transform="rotate(-10 220 918)">To My</text>
    <text class="gold-text script-love" x="232" y="990" font-size="72" text-anchor="middle" transform="rotate(-10 232 990)">Valentine</text>
  </g>

  <!-- Merry Christmas -->
  <g class="sticker sticker-merry-christmas">
    <circle class="sticker-edge" cx="569" cy="946" r="137"/>
    <text class="gold-text brush" font-size="54"><textPath href="#merry-arc" startOffset="50%" text-anchor="middle">Merry</textPath></text>
    <text class="gold-text brush" font-size="50"><textPath href="#christmas-arc" startOffset="4%">Christmas</textPath></text>
    <circle cx="569" cy="955" r="22" fill="url(#festive-tone)" role="img" aria-label="Small gold festive character illustration"/>
  </g>

  <!-- Merry Xmas -->
  <g class="sticker sticker-merry-xmas">
    <circle class="sticker-edge" cx="923" cy="946" r="137"/>
    <circle cx="925" cy="878" r="26" fill="url(#festive-tone)" role="img" aria-label="Gold festive character illustration with scattered sparkles"/>
    <text class="gold-text block-outline" x="923" y="973" font-size="60" text-anchor="middle">MERRY</text>
    <text class="gold-text block-outline" x="923" y="1037" font-size="60" text-anchor="middle">XMAS</text>
  </g>
</svg>
</body>
</html>
```